LEAP GLOW SPIN

Need a 4 X 6 post card design. Here are the elements that need to be on the card:
LEAP, GLOW, SPIN (This is the title please feel free and create)
DATE: August 28, 2022
Showtimes 2:30 PM & 7:30 PM
Location: Harriet Colwin Theatre Walnut Creek, CA
Tickets can be purchased at:
http://colwinstagehall.ticketnook.example/LEAPGLOWSPIN or
by calling the ticket office at (925) 555-PLAY
LEAP, GLOW, SPIN showcases the dance stylings of urban hip hop, ballet, modern jazz and much much more! Bay Area renown dancer/choreographer Rosa Jean Fairbank headlines this cast of dancers and will amaze you as she takes you on a journey through dance that you will never forget. Join us for an experience that will prove to excite and delight you!
Now for the artwork I would like to incorporate all three of these photos. The photo entitled "beach" you are only to use the dancer on the left. So clip out the other dancer in the pink dress. The Garden photo and the beach photo the images need to be cut out from the background. The sidewalk photo you can leave the background (just my preference) but for the sake of the overall design I'm ok with removing its background as well.
Ok have at it. I want to end this competition in a few days so let's get these designs in. Thank you!

```html
<!DOCTYPE html>
<html lang="en">
<head>
<meta charset="utf-8">
<title>LEAP GLOW SPIN – Postcard</title>
<link href="https://fonts.googleapis.com/css2?family=Montserrat:wght@100;200&family=Roboto:wght@400;500;700;900&display=swap" rel="stylesheet">
<style>
  :root {
    --stage: #141418;
    --night: #25226e;
    --indigo: #2f3aa8;
    --violet: #5a3ab0;
    --plum: #4b1a7c;
    --lavender: #b4b0de;
    --white: #ffffff;
    --ink: #0c0b22;
    --hot-pink: #e03a9f;
  }
  * { margin: 0; padding: 0; box-sizing: border-box; }
  html, body { width: 1200px; height: 1200px; overflow: hidden; }
  body { background: var(--stage); position: relative; font-family: "Roboto", Arial, sans-serif; }

  .postcard {
    position: absolute; left: 219px; top: 30px;
    width: 762px; height: 1140px; overflow: hidden;
    background:
      radial-gradient(circle at 28% 58%, rgba(90,120,255,.75) 0, rgba(90,120,255,0) 38%),
      radial-gradient(circle at 82% 70%, rgba(222,60,180,.85) 0, rgba(222,60,180,0) 45%),
      radial-gradient(circle at 62% 48%, rgba(170,90,230,.55) 0, rgba(170,90,230,0) 35%),
      linear-gradient(180deg, var(--night) 0%, var(--indigo) 45%, var(--violet) 75%, var(--plum) 100%);
  }

  .sparkles, .title { position: absolute; inset: 0; }
  .title .word-thin { font-family: "Montserrat", sans-serif; font-weight: 100; fill: var(--white); }
  .title .word-bold { font-family: "Roboto", sans-serif; font-weight: 900; fill: var(--lavender); }
  .title .letter { font-family: "Roboto", sans-serif; font-weight: 900; fill: var(--white); }

  .photo { position: absolute; }
  .photo-leaper {
    left: 405px; top: 185px; width: 150px; height: 320px;
    border-radius: 50% 50% 40% 40% / 20% 20% 60% 60%;
    background: linear-gradient(160deg, rgba(40,30,50,.75), rgba(13,11,20,.75));
  }
  .photo-scarf {
    left: 80px; top: 510px; width: 470px; height: 300px;
    border-radius: 40% 45% 30% 50% / 30% 30% 60% 60%;
    background: linear-gradient(170deg, rgba(98,70,190,.75) 0%, rgba(150,110,200,.55) 50%, rgba(220,110,170,.6) 100%);
  }
  .photo-pink-dancer {
    left: 300px; top: 640px; width: 230px; height: 390px;
    border-radius: 45% 45% 35% 40% / 25% 25% 60% 60%;
    background: linear-gradient(180deg, rgba(240,140,190,.75), rgba(230,100,165,.8));
  }
  .photo-headliner {
    left: 560px; top: 600px; width: 160px; height: 535px;
    border-radius: 40% 40% 30% 30% / 14% 14% 40% 40%;
    background: linear-gradient(180deg, #3a2a40 0%, #d846a2 20%, var(--hot-pink) 70%, #c8358e 100%);
  }

  .details {
    position: absolute; left: 60px; top: 815px; width: 300px;
    text-align: center; color: var(--ink);
  }
  .details .date { font-weight: 700; font-size: 31px; letter-spacing: -.2px; }
  .details .label { font-weight: 400; font-size: 21px; margin-top: 10px; }
  .details .times { font-weight: 700; font-size: 21px; }
  .details .venue { margin-top: 20px; }
  .details .venue .label { margin-top: 0; }
  .details .place { font-size: 17px; color: var(--white); line-height: 23px; }

  .tickets {
    position: absolute; left: 0; top: 1036px; width: 610px;
    text-align: center; color: var(--white);
  }
  .tickets .heading {
    display: flex; align-items: center; justify-content: center; gap: 8px;
    font-weight: 700; font-size: 16.5px;
  }
  .tickets .heading .rule { height: 1.5px; background: var(--white); }
  .tickets .heading .rule-left { width: 158px; }
  .tickets .heading .rule-right { width: 40px; }
  .tickets .url, .tickets .phone { font-size: 16px; line-height: 23px; }
</style>
</head>
<body>
  <main class="postcard">
    <svg class="sparkles" width="762" height="1140" aria-hidden="true">
      <g fill="#cfe0ff">
        <circle cx="190" cy="455" r="2.5"/><circle cx="105" cy="620" r="2"/>
        <circle cx="72" cy="760" r="5" opacity=".8"/><circle cx="240" cy="570" r="2"/>
        <circle cx="155" cy="520" r="1.5"/><circle cx="50" cy="870" r="2"/>
      </g>
      <g fill="#ff9ad6">
        <circle cx="625" cy="400" r="3"/><circle cx="618" cy="502" r="6" opacity=".8"/>
        <circle cx="715" cy="632" r="5" opacity=".8"/><circle cx="690" cy="440" r="2"/>
        <circle cx="585" cy="540" r="2"/>
      </g>
    </svg>

    <div class="photo photo-scarf" role="img" aria-label="Photo: dancer in white lifting a flowing purple scarf"></div>
    <div class="photo photo-pink-dancer" role="img" aria-label="Photo: dancer in a light pink dress with a pink scarf"></div>
    <div class="photo photo-leaper" role="img" aria-label="Photo: ballet dancer in black leaping in arabesque"></div>
    <div class="photo photo-headliner" role="img" aria-label="Photo: headlining dancer in a fuchsia dress walking forward"></div>

    <svg class="title" width="762" height="1140" role="heading" aria-level="1" aria-label="LEAP GLOW SPIN">
      <text class="word-thin" x="83" y="227" font-size="260" textLength="594" lengthAdjust="spacingAndGlyphs">LEAP</text>
      <text class="word-bold" x="83" y="335" font-size="135" textLength="465" lengthAdjust="spacingAndGlyphs">GLOW</text>
      <text class="letter" x="213" y="508" font-size="255" textLength="173" lengthAdjust="spacingAndGlyphs">S</text>
      <text class="letter" x="463" y="605" font-size="255" textLength="157" lengthAdjust="spacingAndGlyphs">P</text>
      <text class="letter" x="176" y="805" font-size="240" textLength="60" lengthAdjust="spacingAndGlyphs">I</text>
      <text class="letter" x="505" y="853" font-size="250" textLength="168" lengthAdjust="spacingAndGlyphs">N</text>
    </svg>

    <section class="details">
      <p class="date">August 28, 2022</p>
      <p class="label">SHOWTIMES</p>
      <p class="times">2:30 PM &amp; 7:30 PM</p>
      <div class="venue">
        <p class="label">LOCATION</p>
        <p class="place">Harriet Colwin Theatre<br>Walnut Creek, CA</p>
      </div>
    </section>

    <section class="tickets">
      <p class="heading"><span class="rule rule-left"></span>TICKETS CAN BE PURCHASED AT<span class="rule rule-right"></span></p>
      <p class="url">http://colwinstagehall.ticketnook.example/LEAPGLOWSPIN or</p>
      <p class="phone">by calling the ticket office at (925) 555-PLAY</p>
    </section>
  </main>
</body>
</html>
```